design a construction company business card

Design business card around our logo. Card must have all the typical info: name, title, address, phone, email, business name, etc. Somewhere on the card I would like to see our motto "Built on integrity... Inspired by commitment." Consider adding a splash of bright orange to the card to complement the blues and silvers/grays in the logo. We are open to metallic inks, textures, etc. We would like to see options on both light and dark backgrounds. The font in the logo is Euro Technic Extended Regular.

```html
<!DOCTYPE html>
<html lang="en">
<head>
<meta charset="utf-8">
<title>Calder Building, Inc. – Business Card</title>
<link href="https://fonts.googleapis.com/css2?family=Michroma&display=swap" rel="stylesheet">
<style>
  :root {
    --backdrop: #2b2e33;
    --card: #131313;
    --brand-blue: #2f5fc4;
    --text-gray: #8c8c8c;
    --rule-gray: #6f6f6f;
  }
  * { margin: 0; padding: 0; box-sizing: border-box; }
  html, body {
    width: 1200px; height: 1141px; overflow: hidden;
    background: var(--backdrop);
    font-family: "Michroma", "Arial", sans-serif;
  }
  .card {
    position: absolute;
    left: 232px; width: 730px; height: 416px;
    background: var(--card);
    box-shadow: 0 6px 16px rgba(0,0,0,.5);
  }
  .card--front { top: 120px; }
  .card--back { top: 570px; }

  .brand {
    position: absolute;
    text-align: center;
    color: var(--brand-blue);
    line-height: 1;
  }
  .brand__name { font-size: 40px; letter-spacing: 2px; }
  .brand__sub { font-size: 15px; letter-spacing: 1px; margin-top: 10px; }
  .card--front .brand { left: 48px; width: 256px; top: 228px; }
  .card--back .brand { left: 0; width: 730px; top: 196px; }

  .rule { position: absolute; height: 2px; }
  .rule--gray { background: var(--rule-gray); height: 1px; }
  .rule--blue { background: var(--brand-blue); }

  .contact {
    position: absolute; right: 43px; top: 146px;
    text-align: right; color: var(--text-gray);
  }
  .contact__name {
    font-size: 27px; color: var(--brand-blue); letter-spacing: 1px;
    line-height: 1;
  }
  .contact__title { font-size: 15px; margin-top: 10px; }
  .contact__address { font-size: 16px; line-height: 22px; margin-top: 18px; }
  .contact__lines { font-size: 15px; line-height: 25px; margin-top: 22px; }

  .card__web {
    position: absolute; left: 0; width: 730px; top: 354px;
    text-align: center; font-size: 16px; color: var(--text-gray);
  }
</style>
</head>
<body>
  <section class="card card--front">
    <div class="rule rule--gray" style="left:0;width:28px;top:207px;"></div>
    <div class="brand">
      <div class="brand__name">CALDER</div>
      <div class="brand__sub">BUILDING, INC.</div>
    </div>
    <div class="rule rule--blue" style="left:329px;width:358px;top:207px;"></div>
    <div class="rule rule--gray" style="left:700px;width:30px;top:207px;"></div>
    <div class="contact">
      <div class="contact__name">HARLAN VOSS</div>
      <div class="contact__title">General Manager</div>
      <div class="contact__address">412 W Linden St<br>Fairview, Ohio 45390</div>
      <div class="contact__lines">
        000-000-0000<br>
        000-000-0000<br>
        calderbuilding.inc@mailbox.com<br>
        www.calderbuilding.com
      </div>
    </div>
  </section>

  <section class="card card--back">
    <div class="brand">
      <div class="brand__name">CALDER</div>
      <div class="brand__sub">BUILDING, INC.</div>
    </div>
    <div class="card__web">www.calderbuilding.com</div>
  </section>
</body>
</html>
```